I need a box design created for a DNA Fitness Test

I need a modern and sleek box design for a fitness test. The box needs to have our logo on it and should be clean and modern. The Box is 9 Inches Long 3 and 3/4 inches wide, and 2 inches tall. Company logo attached. The company name is cedar vitality.

Target Market(s)

Fitness

Industry/Entity Type

Fitness

Requirements
Must have
• Our logo

```html
<!DOCTYPE html>
<html lang="en">
<head>
<meta charset="utf-8">
<title>Cedar Vitality – DNA Fitness Test Box</title>
<link rel="stylesheet" href="https://fonts.googleapis.com/css2?family=Arimo:wght@400;700&family=Montserrat:wght@700&display=swap">
<style>
  :root {
    --page: #ffffff;
    --panel-edge: #c9d6e3;
    --sky-light: #f4f9ff;
    --sky-mid: #d6eafb;
    --sky-deep: #a9d3f2;
    --ink: #000000;
    --title-blue: #0a3f8c;
    --frame-green: #8fd89a;
    --ring-green: #7fe28c;
    --mark-blue: #4a78b4;
    --figure-blue: #9fbde0;
  }
  * { margin: 0; padding: 0; box-sizing: border-box; }
  html, body {
    width: 1200px; height: 1200px; overflow: hidden;
    background: var(--page);
    font-family: "Arimo", Arial, sans-serif;
  }
  .canvas { position: relative; width: 1200px; height: 1200px; }

  .panel {
    position: absolute; left: 270px; width: 652px;
    border: 1px solid var(--panel-edge);
    overflow: hidden;
  }
  .panel-backdrop {
    position: absolute; inset: 0;
    background:
      radial-gradient(circle at 85% 30%, var(--sky-deep) 0, transparent 32%),
      radial-gradient(circle at 8% 75%, var(--sky-deep) 0, transparent 28%),
      radial-gradient(circle at 45% 60%, var(--sky-mid) 0, transparent 40%),
      linear-gradient(135deg, var(--sky-mid), var(--sky-light) 45%, var(--sky-mid));
  }
  .panel--lid    { top: 206px; height: 272px; }
  .panel--front  { top: 481px; height: 145px; }
  .panel--base   { top: 629px; height: 271px; }
  .panel--back   { top: 903px; height: 145px; }

  /* brand lockup: plain circle above the name */
  .brand-dot {
    position: absolute; left: 50%; border-radius: 50%;
    background: var(--mark-blue);
  }
  .brand-name, .brand-sub {
    position: absolute; left: 0; right: 0; text-align: center;
    font-family: "Montserrat", Arial, sans-serif; font-weight: 700;
    color: var(--ink); line-height: 1; white-space: nowrap;
  }

  .panel--lid .brand-dot { top: 24px; width: 100px; height: 100px; margin-left: -50px; }
  .panel--lid .brand-name { top: 169px; font-size: 58px; letter-spacing: 1px; }
  .panel--lid .brand-sub  { top: 228px; font-size: 22px; letter-spacing: 15px; padding-left: 15px; }

  .panel--front .brand-dot,
  .panel--back .brand-dot { width: 54px; height: 54px; margin-left: -27px; }
  .panel--front .brand-dot { top: 17px; }
  .panel--back .brand-dot  { top: 10px; }
  .panel--front .brand-name,
  .panel--back .brand-name { font-size: 30px; letter-spacing: 0.5px; }
  .panel--front .brand-name { top: 87px; }
  .panel--back .brand-name  { top: 81px; }
  .panel--front .brand-sub,
  .panel--back .brand-sub { font-size: 11px; letter-spacing: 7px; padding-left: 7px; }
  .panel--front .brand-sub { top: 118px; }
  .panel--back .brand-sub  { top: 113px; }

  .info-frame {
    position: absolute; left: 56px; top: 45px; width: 455px; height: 182px;
    border: 4px solid var(--frame-green);
    border-right: none;
    background: rgba(255,255,255,0.45);
  }
  .info-title {
    position: absolute; left: 12px; top: 6px;
    font-size: 27px; font-weight: 700; color: var(--title-blue);
    letter-spacing: 0.6px; line-height: 1.1; white-space: nowrap;
  }
  .info-copy {
    position: absolute; left: 6px; top: 45px; width: 360px;
    font-size: 10px; line-height: 9px; color: var(--ink); letter-spacing: 0.3px;
  }
  .benefit-list { list-style: none; margin: 11px 0 0 25px; }
  .benefit-list li::before { content: "· "; }
  .info-closing { margin-top: 11px; }

  .figure-badge {
    position: absolute; left: 422px; top: 45px; width: 184px; height: 184px;
    border-radius: 50%;
    border: 4px solid var(--ring-green);
    background: radial-gradient(circle at 50% 55%, var(--figure-blue) 0, #ffffff 62%);
  }
</style>
</head>
<body>
<div class="canvas">

  <section class="panel panel--lid">
    <div class="panel-backdrop" role="img" aria-label="Soft blue molecule illustration background"></div>
    <span class="brand-dot"></span>
    <div class="brand-name">CEDAR</div>
    <div class="brand-sub">VITALITY</div>
  </section>

  <section class="panel panel--front">
    <div class="panel-backdrop" role="img" aria-label="Soft blue molecule illustration background"></div>
    <span class="brand-dot"></span>
    <div class="brand-name">CEDAR</div>
    <div class="brand-sub">VITALITY</div>
  </section>

  <section class="panel panel--base">
    <div class="panel-backdrop" role="img" aria-label="Soft blue molecule illustration background"></div>
    <div class="info-frame">
      <h2 class="info-title">UNLOCK YOUR POTENTIAL</h2>
      <div class="info-copy">
        <p>Our team of scientists have spent years using the lastest scientific research and the lastest technology to develop our Helix Fitness line of products. By using a simple and painless cheek swab we are able to reveal the details about an individual’s unique fitness and nutrition requirements, unlocking their body’s true potential for success.</p>
        <ul class="benefit-list">
          <li>Leverage impulsive tendencies</li>
          <li>Learn to stop eating when full</li>
          <li>Train your body to burn fat efficiently</li>
          <li>Maintain weight loss</li>
          <li>Recover Faster</li>
        </ul>
        <p class="info-closing">Get all of this and more from CEDAR VITALITY</p>
      </div>
    </div>
    <div class="figure-badge" role="img" aria-label="Illustration of a woman lifting dumbbells in silhouette"></div>
  </section>

  <section class="panel panel--back">
    <div class="panel-backdrop" role="img" aria-label="Soft blue molecule illustration background"></div>
    <span class="brand-dot"></span>
    <div class="brand-name">CEDAR</div>
    <div class="brand-sub">VITALITY</div>
  </section>

</div>
</body>
</html>
```